I need a cover for a brochure made

I need a cover for a brochure. The dimensions are 8.25 wide and 5.25 high... I also need a .25 inch bleed outside of those dimensions.

I need it to look like a vintage photo album cover. In big words, I would like it to say "Family". Above it in smaller words "To our Harlow Fairway" ... making it look like the words are gold inlay or something.

I would like it kind of in the style of some of the attached maybe. Just vintage looking.

```html
<!DOCTYPE html>
<html lang="en">
<head>
<meta charset="UTF-8">
<title>Family Brochure Cover</title>
<link href="https://fonts.googleapis.com/css2?family=EB+Garamond:wght@400&family=Playfair+Display:wght@800&display=swap" rel="stylesheet">
<style>
  :root {
    --page-bg: #ffffff;
    --leather-light: #9a4a22;
    --leather-mid: #6e3017;
    --leather-dark: #381a0d;
    --gold: #a8853a;
    --gold-soft: rgba(168, 133, 58, 0.55);
  }
  html, body {
    margin: 0;
    padding: 0;
    width: 1200px;
    height: 1000px;
    overflow: hidden;
    background: var(--page-bg);
  }
  .canvas {
    position: relative;
    width: 1200px;
    height: 1000px;
  }
  .cover {
    position: absolute;
    left: 179px;
    top: 232px;
    width: 842px;
    height: 536px;
    overflow: hidden;
  }
  .leather {
    position: absolute;
    inset: 0;
    background: radial-gradient(ellipse 62% 62% at 50% 40%,
      var(--leather-light) 0%,
      var(--leather-mid) 55%,
      var(--leather-dark) 100%);
  }
  .frame {
    position: absolute;
    inset: 0;
  }
  .flourish {
    position: absolute;
    left: 239px;
    width: 364px;
    height: 30px;
    background: linear-gradient(90deg,
      rgba(168, 133, 58, 0) 0%,
      var(--gold-soft) 20%,
      var(--gold-soft) 80%,
      rgba(168, 133, 58, 0) 100%);
    -webkit-mask: linear-gradient(180deg, transparent 40%, #000 45%, #000 55%, transparent 60%);
    mask: linear-gradient(180deg, transparent 30%, #000 42%, #000 58%, transparent 70%);
  }
  .flourish--top { top: 150px; }
  .flourish--bottom { top: 353px; }
  .dedication {
    position: absolute;
    left: 0;
    width: 100%;
    top: 192px;
    margin: 0;
    text-align: center;
    font-family: "EB Garamond", Georgia, serif;
    font-weight: 400;
    font-size: 31px;
    letter-spacing: 0.5px;
    color: var(--gold);
  }
  .title {
    position: absolute;
    left: 0;
    width: 100%;
    top: 222px;
    margin: 0;
    text-align: center;
    font-family: "Playfair Display", Georgia, serif;
    font-weight: 800;
    font-size: 104px;
    line-height: 1.2;
    color: var(--gold);
  }
</style>
</head>
<body>
<div class="canvas">
  <section class="cover">
    <div class="leather" role="img" aria-label="Brown leather texture with darkened edges"></div>
    <svg class="frame" width="842" height="536" viewBox="0 0 842 536" aria-hidden="true">
      <rect x="26.5" y="26.5" width="789" height="483" fill="none" stroke="#a8853a" stroke-width="1.2"/>
      <rect x="33.5" y="33.5" width="775" height="469" fill="none" stroke="#a8853a" stroke-width="1.2"/>
    </svg>
    <div class="flourish flourish--top" role="img" aria-label="Gold leaf flourish divider"></div>
    <p class="dedication">To our Harlow Fairway</p>
    <h1 class="title">Family</h1>
    <div class="flourish flourish--bottom" role="img" aria-label="Gold leaf flourish divider"></div>
  </section>
</div>
</body>
</html>
```